Modern business cards and stationery design for an IT company
Brolund Systems
Modern business cards and stationery design for an IT company - Information Technology
Creative Brief
Professional
Tomas Ellery
President
We do not want our address on the business card
tomas@brolundsys.example
www.brolundsys.example
BrolundSys BrolundSys
For reference, please visit our new website which is currently being constructed located at www.brolundsys.example/tellery This website provides the new design and layout for the company and potentially will help with the design process. Please note that the main website (www.brolundsys.example) is in process of being replaced with the first website mentioned. (www.brolundsys.example/tellery).

```html
<!DOCTYPE html>
<html lang="en">
<head>
<meta charset="utf-8">
<title>Brolund Systems — Stationery</title>
<link href="https://fonts.googleapis.com/css2?family=Exo+2:wght@600&family=Open+Sans:wght@400;600&display=swap" rel="stylesheet">
<style>
  :root {
    --red-deep: #8e0a10;
    --red: #c4161c;
    --red-bright: #e2312f;
    --grey: #b8b8b8;
    --grey-light: #e4e4e4;
    --ink: #333333;
    --ink-soft: #777777;
    --paper: #ffffff;
    --stage: #ffffff;
    --shadow: 0 2px 6px rgba(0,0,0,0.18);
  }
  * { box-sizing: border-box; margin: 0; padding: 0; }
  html, body { width: 1200px; height: 936px; overflow: hidden; background: var(--stage); }
  body { position: relative; font-family: "Open Sans", Arial, sans-serif; color: var(--ink); }

  .sheet { position: absolute; background: var(--paper); box-shadow: var(--shadow); overflow: hidden; }
  .swoosh { position: absolute; left: 0; top: 0; width: 100%; display: block; }

  .brand { position: absolute; display: flex; align-items: center; gap: 8px; }
  .brand-dot { border-radius: 50%; background: var(--red); flex: none; }
  .brand-name { font-family: "Exo 2", Arial, sans-serif; font-weight: 600; color: var(--red); letter-spacing: 0.12em; text-transform: uppercase; line-height: 1.05; }

  .faint-mark { position: absolute; border-radius: 50%; background: var(--red); opacity: 0.07; }

  /* Letterhead */
  .letterhead { left: 139px; top: 63px; width: 431px; height: 557px; }
  .letterhead .swoosh { height: 92px; }
  .letterhead .brand { left: 26px; top: 98px; }
  .letterhead .brand-dot { width: 18px; height: 18px; }
  .letterhead .brand-name { font-size: 13px; }
  .letter-body { position: absolute; left: 26px; top: 150px; width: 300px; font-size: 6.4px; line-height: 1.55; color: var(--ink); }
  .letter-body p { margin-bottom: 7px; }
  .signature { width: 46px; height: 16px; background: linear-gradient(90deg, #bcbcbc, #dcdcdc); border-radius: 8px; margin: 4px 0 6px; }
  .letter-footer { position: absolute; left: 26px; bottom: 30px; font-size: 5.6px; line-height: 1.9; color: var(--ink-soft); }
  .letter-footer span { display: flex; align-items: center; gap: 5px; }
  .icon { width: 7px; height: 7px; flex: none; }
  .letterhead .faint-mark { width: 300px; height: 300px; right: -70px; bottom: -40px; }

  /* Cover */
  .cover { left: 633px; top: 63px; width: 430px; height: 557px; }
  .cover .swoosh { height: 92px; }
  .cover .brand { left: 0; right: 0; top: 226px; flex-direction: column; gap: 12px; }
  .cover .brand-dot { width: 46px; height: 46px; }
  .cover .brand-name { font-size: 30px; text-align: center; }
  .cover .faint-mark { width: 320px; height: 320px; left: -90px; bottom: -70px; }

  /* Business cards */
  .card { left: 46px; width: 195px; height: 119px; }
  .card .swoosh { height: 36px; }
  .card-front { top: 653px; }
  .card-back { top: 790px; }
  .card .brand-dot { width: 12px; height: 12px; }
  .card .brand-name { font-size: 8px; }
  .card-front .brand { left: 12px; top: 42px; }
  .card-contact { position: absolute; right: 12px; top: 48px; font-size: 5px; line-height: 1.9; color: var(--ink); }
  .card-contact .name { font-weight: 600; font-size: 6px; color: var(--red); }
  .card-contact span { display: flex; align-items: center; gap: 4px; }
  .card-contact .icon { width: 5px; height: 5px; }
  .card-back .brand { left: 12px; top: 44px; }

  /* Envelope front */
  .envelope { left: 266px; top: 671px; width: 430px; height: 240px; }
  .envelope .swoosh { height: 58px; }
  .envelope .brand { left: 20px; top: 62px; }
  .envelope .brand-dot { width: 16px; height: 16px; }
  .envelope .brand-name { font-size: 12px; }
  .envelope .faint-mark { width: 190px; height: 190px; right: 40px; bottom: -90px; }

  /* Envelope back */
  .envelope-back { left: 734px; top: 671px; width: 431px; height: 240px; }
  .flap-band { position: absolute; left: 0; top: 0; width: 100%; height: 42px; background: linear-gradient(180deg, var(--red-bright), var(--red-deep)); }
  .flap-band p { color: #ffffff; font-size: 9px; letter-spacing: 0.2em; text-align: center; line-height: 42px; }
  .flap-edge { position: absolute; left: 0; top: 42px; width: 100%; height: 3px; background: var(--grey-light); }
</style>
</head>
<body>

<svg width="0" height="0" style="position:absolute" aria-hidden="true">
  <defs>
    <linearGradient id="red-wave" x1="0" y1="0" x2="1" y2="1">
      <stop offset="0" stop-color="#e2312f"/>
      <stop offset="0.6" stop-color="#c4161c"/>
      <stop offset="1" stop-color="#8e0a10"/>
    </linearGradient>
    <linearGradient id="grey-wave" x1="0" y1="0" x2="1" y2="0">
      <stop offset="0" stop-color="#e6e6e6"/>
      <stop offset="1" stop-color="#a8a8a8"/>
    </linearGradient>
    <symbol id="wave" viewBox="0 0 400 100" preserveAspectRatio="none">
      <path d="M0 0 H400 V72 C310 28 170 18 0 44 Z" fill="url(#red-wave)"/>
      <path d="M0 52 C170 28 310 40 400 82 V96 C300 54 170 40 0 62 Z" fill="url(#grey-wave)"/>
    </symbol>
  </defs>
</svg>

<section class="sheet letterhead" aria-label="Letterhead">
  <svg class="swoosh" viewBox="0 0 400 100" preserveAspectRatio="none"><use href="#wave"/></svg>
  <div class="brand"><span class="brand-dot"></span><span class="brand-name">Brolund Systems</span></div>
  <div class="faint-mark"></div>
  <div class="letter-body">
    <p>July 8, 2024</p>
    <p>Dear Client,<br>Main Office, Harbour Road</p>
    <p>Thank you for your continued interest in our services. This letter confirms the details of our recent discussion and outlines the next steps we will take together to support your team.</p>
    <p>Our engineers will review your current systems and prepare a short report with clear recommendations for the coming quarter.</p>
    <p>Please contact us at any time if you have questions. We look forward to working with you.</p>
    <p>Best Regards,</p>
    <div class="signature" role="img" aria-label="Handwritten signature"></div>
    <p>Tomas Ellery<br>President</p>
  </div>
  <div class="letter-footer">
    <span><svg class="icon" viewBox="0 0 10 10"><path d="M2 1 L4 1 L5 3 L4 4 C4.5 5.5 5 6 6 6 L7 5 L9 6 L9 8 C5 9 1 5 2 1 Z" fill="#c4161c"/></svg>+1 555 0100 200</span>
    <span><svg class="icon" viewBox="0 0 10 10"><rect x="1" y="2" width="8" height="6" fill="none" stroke="#c4161c"/><path d="M1 2 L5 5.5 L9 2" fill="none" stroke="#c4161c"/></svg>tomas@brolundsys.example</span>
    <span><svg class="icon" viewBox="0 0 10 10"><circle cx="5" cy="5" r="4" fill="none" stroke="#c4161c"/><path d="M1 5 H9 M5 1 C3 3 3 7 5 9 C7 7 7 3 5 1" fill="none" stroke="#c4161c" stroke-width="0.7"/></svg>www.brolundsys.example</span>
  </div>
</section>

<section class="sheet cover" aria-label="Presentation cover">
  <svg class="swoosh" viewBox="0 0 400 100" preserveAspectRatio="none"><use href="#wave"/></svg>
  <div class="faint-mark"></div>
  <div class="brand"><span class="brand-dot"></span><span class="brand-name">Brolund Systems</span></div>
</section>

<section class="sheet card card-front" aria-label="Business card front">
  <svg class="swoosh" viewBox="0 0 400 100" preserveAspectRatio="none"><use href="#wave"/></svg>
  <div class="brand"><span class="brand-dot"></span><span class="brand-name">Brolund<br>Systems</span></div>
  <div class="card-contact">
    <span class="name">Tomas Ellery</span>
    <span>President</span>
    <span><svg class="icon" viewBox="0 0 10 10"><path d="M2 1 L4 1 L5 3 L4 4 C4.5 5.5 5 6 6 6 L7 5 L9 6 L9 8 C5 9 1 5 2 1 Z" fill="#c4161c"/></svg>+1 555 0100 200</span>
    <span><svg class="icon" viewBox="0 0 10 10"><rect x="1" y="2" width="8" height="6" fill="none" stroke="#c4161c"/><path d="M1 2 L5 5.5 L9 2" fill="none" stroke="#c4161c"/></svg>tomas@brolundsys.example</span>
    <span><svg class="icon" viewBox="0 0 10 10"><circle cx="5" cy="5" r="4" fill="none" stroke="#c4161c"/></svg>www.brolundsys.example</span>
  </div>
</section>

<section class="sheet card card-back" aria-label="Business card back">
  <svg class="swoosh" viewBox="0 0 400 100" preserveAspectRatio="none"><use href="#wave"/></svg>
  <div class="brand"><span class="brand-dot"></span><span class="brand-name">Brolund Systems</span></div>
</section>

<section class="sheet envelope" aria-label="Envelope front">
  <svg class="swoosh" viewBox="0 0 400 100" preserveAspectRatio="none"><use href="#wave"/></svg>
  <div class="brand"><span class="brand-dot"></span><span class="brand-name">Brolund Systems</span></div>
  <div class="faint-mark"></div>
</section>

<section class="sheet envelope-back" aria-label="Envelope back">
  <div class="flap-band"><p>www.brolundsys.example</p></div>
  <div class="flap-edge"></div>
</section>

</body>
</html>
```